K & D A/C Compressors' Business Card

Hello,

I need someone to create a new business card for my business. The name of my Business is: K & D A/C Compressors. I sell automotive air conditioning parts (a/c parts). I would like the business card to incorporate my logo, and to have an automotive feel to it. It is important that the business card feel like it is coming from an automotive parts business.

I already have a logo, which I will provide.

Thanks.
Updates

Project Deadline Extended Reason: I feel like extending the deadline until October 9, 2017, will allow for more time to design the business card. Thank you for your understanding. Added Monday, October 2, 2017

Target Market(s)

Consumers who need automotive a/c parts, and auto mechanics.

Industry/Entity Type

Automotive

Contact Information for Business Card

Business name: K & D A/C Compressors
Business Address: 48207 Southwest 36th Street, Palm Cove, Florida 33990
Telephone: 305-472-1390
Fax: To be provided once I choose your design.
Website: www.kdcoolunits.example
Email: support@kdcoolunits.example
Names: To be provided once I choose your design.

Font styles to use
Sans Serif

Colors

Designer to choose colors to be used in the design.

Requirements
Must have
• The business card must include all of the "Business Card Details" and the logo I have uploaded.

```html
<!DOCTYPE html>
<html lang="en">
<head>
<meta charset="utf-8">
<title>K &amp; D A/C Compressors – Business Card</title>
<link rel="stylesheet" href="https://fonts.googleapis.com/css2?family=Montserrat:wght@500&family=Roboto:wght@400&display=swap">
<style>
  :root{
    --backdrop:#e6e6e6;
    --card-white:#ffffff;
    --card-black:#121212;
    --brand-blue:#00aeef;
    --brand-grey:#9a9a9a;
    --text-dark:#1a1a1a;
    --text-light:#ffffff;
  }
  *{margin:0;padding:0;box-sizing:border-box}
  html,body{width:1200px;height:718px;overflow:hidden}
  body{background:var(--backdrop);font-family:"Roboto",Arial,sans-serif;position:relative}
  .card{position:absolute;width:540px;height:308px;top:205px;overflow:hidden;box-shadow:0 2px 6px rgba(0,0,0,.12)}
  .card-front{left:40px;background:var(--card-black)}
  .card-back{left:620px;background:var(--card-white)}

  .wordmark{position:absolute;display:flex;align-items:center;gap:12px;font-family:"Montserrat",Arial,sans-serif;font-weight:500;color:var(--brand-grey);white-space:nowrap}
  .wordmark-square{background:var(--brand-blue);flex:none}
  .card-front .wordmark{left:50%;top:50%;transform:translate(-50%,-50%);font-size:30px}
  .card-front .wordmark-square{width:34px;height:34px}
  .card-back .wordmark{left:50%;top:40px;transform:translateX(-50%);font-size:19px}
  .card-back .wordmark-square{width:22px;height:22px}

  .contact-panel{position:absolute;left:355px;top:100px;width:185px;height:100px;background:var(--card-black);z-index:2}
  .contact-notch{position:absolute;left:-7px;top:50px;width:0;height:0;border-top:7px solid transparent;border-bottom:7px solid transparent;border-right:7px solid var(--card-black)}
  .contact-list{list-style:none;padding:15px 0 0 16px;color:var(--text-light);font-size:10px;line-height:18px}
  .contact-list li{display:flex;align-items:center;gap:7px;white-space:nowrap}
  .contact-list svg{width:10px;height:10px;flex:none}

  .name-band{position:absolute;left:0;top:150px;width:355px;height:86px;background:var(--brand-blue);z-index:1}
  .band-notch{position:absolute;left:190px;top:-7px;width:0;height:0;border-left:7px solid transparent;border-right:7px solid transparent;border-bottom:7px solid var(--brand-blue)}
  .band-name{position:absolute;left:118px;top:22px;color:var(--text-light);font-family:"Montserrat",Arial,sans-serif;font-weight:500;font-size:17px;line-height:21px}

  .address{position:absolute;left:0;right:0;top:262px;text-align:center;font-size:12.5px;color:var(--text-dark)}
</style>
</head>
<body>
  <section class="card card-front" aria-label="Business card front">
    <div class="wordmark"><span class="wordmark-square"></span>K &amp; D A/C Compressors</div>
  </section>

  <section class="card card-back" aria-label="Business card back">
    <div class="wordmark"><span class="wordmark-square"></span>K &amp; D A/C Compressors</div>

    <div class="contact-panel">
      <span class="contact-notch"></span>
      <ul class="contact-list">
        <li><svg viewBox="0 0 10 10"><path fill="var(--brand-blue)" d="M2 1h2l1 2-1.2 1a5 5 0 0 0 2.2 2.2L7 5l2 1v2c0 .6-.4 1-1 1A8 8 0 0 1 1 2c0-.6.4-1 1-1z"/></svg>305-472-1390</li>
        <li><svg viewBox="0 0 10 10"><rect fill="var(--brand-blue)" x="1" y="3" width="8" height="6"/><rect fill="var(--brand-blue)" x="3" y="0.5" width="4" height="2"/></svg>305-472-1391</li>
        <li><svg viewBox="0 0 10 10"><rect fill="var(--brand-blue)" x="0.5" y="2" width="9" height="6"/><path d="M1 2.5l4 3 4-3" stroke="var(--card-black)" fill="none"/></svg>support@kdcoolunits.example</li>
        <li><svg viewBox="0 0 10 10"><g fill="none" stroke="var(--brand-blue)" stroke-width="1"><circle cx="5" cy="5" r="4"/><ellipse cx="5" cy="5" rx="1.8" ry="4"/><path d="M1 5h8"/></g></svg>www.kdcoolunits.example</li>
      </ul>
    </div>

    <div class="name-band">
      <span class="band-notch"></span>
      <p class="band-name">K &amp; D<br>A/C Compressors</p>
    </div>

    <p class="address">48207 Southwest 36th Street, Palm Cove, Florida 33990</p>
  </section>
</body>
</html>
```